Corvane Electronics, Inc. Business card

Incorporate a globe.
We repair electronics, sell electronic parts, and we recycle electronics. We've been in business since 1982. A technology feel to the card is preferred. I want to be able to give this card to a client from different industries and make it relate-able. I don't have a logo that I've been partial to in the past. It is not necessary in this case.

Target Market(s)

Consumer, Industrial, Business, Medical

Industry/Entity Type

Business

Contact Information for Business Card

4518 Maple Crest Blvd. Dallas, TX 75207
214-555-0187 main 214-555-0143 fax
Paul Bredesen VP

Font styles to use
Serif

Requirements
Must have
• Technology feel
Nice to have
• Metallic look
Should not have
• no pastel colors

```html
<!DOCTYPE html>
<html lang="en">
<head>
<meta charset="utf-8">
<title>Corvane Electronics, Inc. — Business Card</title>
<link rel="stylesheet" href="https://fonts.googleapis.com/css2?family=Oswald:wght@300;400;500&display=swap">
<style>
  :root {
    --charcoal: #222222;
    --paper: #ffffff;
    --silver: #c8c8c8;
    --rule: #c4c4c4;
    --ink: #111111;
    --globe-tone: #e4e7ef;
  }
  * { margin: 0; padding: 0; box-sizing: border-box; }
  html, body { width: 1200px; height: 720px; overflow: hidden; background: var(--paper); }
  .card {
    position: relative;
    width: 1200px;
    height: 720px;
    font-family: "Oswald", "Arial Narrow", sans-serif;
    background: var(--paper);
    overflow: hidden;
  }
  .contact-side {
    position: absolute; left: 0; top: 0;
    width: 595px; height: 720px;
    background: var(--charcoal);
  }
  .identity {
    position: absolute; right: 240px; top: 120px;
    text-align: right; color: var(--silver);
    font-weight: 300; text-transform: uppercase;
  }
  .identity__name { font-size: 40px; line-height: 1.1; }
  .identity__title { font-size: 22px; line-height: 1; margin-top: 0; }
  .lines { position: absolute; left: 144px; top: 219px; color: var(--silver); font-weight: 300; }
  .line { display: flex; align-items: center; height: 36px; font-size: 24px; }
  .line svg { width: 34px; height: 28px; margin-right: 23px; fill: var(--silver); }
  .address-band {
    position: absolute; left: 0; top: 532px;
    width: 595px; height: 105px;
    background: var(--paper);
    border-bottom: 6px solid var(--rule);
  }
  .address-band__bar {
    position: absolute; left: 118px; top: 6px;
    width: 4px; height: 87px; background: var(--rule);
  }
  .address-band__pin { position: absolute; left: 147px; top: 36px; width: 24px; height: 30px; fill: var(--charcoal); }
  .address {
    position: absolute; left: 190px; top: 22px;
    font-size: 23px; line-height: 27px; font-weight: 400;
    color: var(--charcoal); font-style: normal; text-transform: uppercase;
  }
  .brand-mark {
    position: absolute; left: 752px; top: 110px;
    width: 330px; height: 330px; border-radius: 50%;
    background: var(--globe-tone);
  }
  .brand {
    position: absolute; left: 600px; top: 462px; width: 600px;
    text-align: center; color: var(--ink); font-weight: 500;
    text-transform: uppercase;
  }
  .brand__name { font-size: 118px; line-height: 1.05; }
  .brand__sub { font-size: 56px; line-height: 1; margin-top: 0; }
</style>
</head>
<body>
<div class="card">
  <section class="contact-side">
    <div class="identity">
      <div class="identity__name">Paul Bredesen</div>
      <div class="identity__title">Vice President</div>
    </div>
    <div class="lines">
      <div class="line">
        <svg viewBox="0 0 34 28" aria-hidden="true"><path d="M2 9c0-4 6-7 15-7s15 3 15 7v3h-7V9c-2-1-5-1.5-8-1.5S11 8 9 9v3H2z"/><path d="M9 12h16l4 13H5z"/><circle cx="17" cy="18" r="3" fill="#222"/></svg>
        <span>+1-214-555-0187</span>
      </div>
      <div class="line">
        <svg viewBox="0 0 34 28" aria-hidden="true"><path d="M9 1h16v9H9z"/><path d="M2 11h30v16H2z"/><path d="M7 15h20v2H7zM7 20h20v2H7z" fill="#222"/></svg>
        <span>+1-214-555-0143</span>
      </div>
    </div>
    <div class="address-band">
      <div class="address-band__bar"></div>
      <svg class="address-band__pin" viewBox="0 0 24 30" aria-hidden="true"><path d="M12 0C5.4 0 0 5.2 0 11.6 0 20 12 30 12 30s12-10 12-18.4C24 5.2 18.6 0 12 0zm0 16a4.5 4.5 0 1 1 0-9 4.5 4.5 0 0 1 0 9z"/></svg>
      <address class="address">4518 Maple Crest Blvd.<br>Dallas, TX 75207</address>
    </div>
  </section>
  <div class="brand-mark" aria-hidden="true"></div>
  <div class="brand">
    <div class="brand__name">Corvane</div>
    <div class="brand__sub">Electronics, Inc.</div>
  </div>
</div>
</body>
</html>
```